Tagline/slogan for a travel agency

Hi, all.

We need an English version of our company's tagline.

We are a travel agency based in Japan. Our customers are both from overseas to Japan and from domestic to overseas.

The original tagline in Japanese is "また来たい、また行きたい" and this tagline means "We will make you want to visit again (both Japan and other countries)".

Please note my preferences:

1) Preferably, maximum of 6 words. The fewer the better...preferable 3 to 4 words.
2) The tagline has to be in simple english, simple enough for people from non-english-native countries to be able to understand.

I will pick a winner once I find a suitable entry.

Arigatou!

```html
<!DOCTYPE html>
<html lang="en">
<head>
<meta charset="utf-8">
<title>Tagline Proposals – Travel Agency</title>
<link rel="stylesheet" href="https://fonts.googleapis.com/css2?family=Roboto+Slab:wght@400&display=swap">
<style>
  :root {
    --sky-top: #5f78c9;
    --sky-mid: #7d95d8;
    --mountain-haze: #8f9cc8;
    --valley: #7c8a86;
    --grass: #6f9a4e;
    --grass-deep: #4f7a38;
    --brick: #8a3a22;
    --mortar: #c9c4bd;
    --tagline: #ffffff;
  }
  html, body {
    margin: 0;
    padding: 0;
    width: 1200px;
    height: 1200px;
    overflow: hidden;
    background: var(--sky-top);
  }
  .poster {
    position: relative;
    width: 1200px;
    height: 1200px;
    overflow: hidden;
  }
  .scenery {
    position: absolute;
    left: 0;
    top: 0;
    width: 1200px;
    height: 1124px;
    background: linear-gradient(
      to bottom,
      var(--sky-top) 0%,
      var(--sky-mid) 38%,
      var(--mountain-haze) 55%,
      var(--valley) 70%,
      var(--grass) 86%,
      var(--grass-deep) 100%
    );
  }
  .brick-ledge {
    position: absolute;
    left: 0;
    top: 1124px;
    width: 1200px;
    height: 76px;
    background: linear-gradient(
      to bottom,
      var(--brick) 0%,
      var(--brick) 45%,
      var(--mortar) 60%,
      var(--mortar) 100%
    );
  }
  .tagline-options {
    position: absolute;
    left: 207px;
    top: -11px;
    margin: 0;
    font-family: "Roboto Slab", serif;
    font-weight: 400;
    font-size: 67px;
    line-height: 102px;
    color: var(--tagline);
    letter-spacing: 0.5px;
  }
  .tagline-options p {
    margin: 0;
  }
</style>
</head>
<body>
  <main class="poster">
    <div class="scenery" role="img" aria-label="Photo of a snow-capped volcano under blue sky, a white bullet train passing green fields and blossoming cherry trees"></div>
    <div class="brick-ledge" role="img" aria-label="Strip of red brick wall with pale mortar"></div>
    <div class="tagline-options">
      <p>We serve Revisit your</p>
      <p>Dream Destinations</p>
      <p>or</p>
      <p>Revisit your Dream</p>
      <p>Destinations with us</p>
      <p>or</p>
      <p>we serve your revisit to</p>
      <p>your Dream Destinations</p>
    </div>
  </main>
</body>
</html>
```